Saffron Lotus Court Business Card

I am looking for a business card desgined for my restaurant. It is an Indian restaurant, we are looking for something thats modern, yet traditional with the indian culture, we are looking for colors that match our logo. The logo is a design of the building with the name of the restaurant. for more information on the restaurant go to www.saffronlotuscourt.example

Industry/Entity Type

Indian Restaurant

Contact Information for Business Card

we are looking for somthing thats modern, yet traditional with the indian culture, we are looking for colors that match our logo. The logo is a design of the building with the name of the restaurant. for more information on the restaurant go to www.saffronlotuscourt.example

Requirements
Must have
• The logo that is attached,
• Name: Harjot Banwal,
• address of the restaurant: 2917 West Tamarind Ave, Phoenix, Arizona, 85047
• Phone: (602) 517-3094
• Fax: (602) 768-2145
• Restaurant Catering Banquet
• Website: www.SaffronLotusCourt.example
Nice to have
• wanted to get something that goes with the theme of the restaurant, which is traditional but also keep a very professional and modern touch

```html
<!DOCTYPE html>
<html lang="en">
<head>
<meta charset="utf-8">
<title>Saffron Lotus Court — Business Card</title>
<link rel="stylesheet" href="https://fonts.googleapis.com/css2?family=Cinzel:wght@400;600;700&display=swap">
<style>
  :root {
    --saffron: #e96522;
    --crimson: #b5232f;
    --ink: #1c1c1c;
    --paper: #ffffff;
    --stage: #ffffff;
    --faint: #ececec;
  }
  * { margin: 0; padding: 0; box-sizing: border-box; }
  html, body { width: 1200px; height: 1200px; overflow: hidden; background: var(--stage); }
  .canvas { position: relative; width: 1200px; height: 1200px; font-family: "Cinzel", serif; }

  .card { position: absolute; width: 560px; height: 320px; overflow: hidden; }
  .card--front { left: 475px; top: 250px; background: var(--paper); outline: 1px solid #e4e4e4; }
  .card--back { left: 165px; top: 610px; background: var(--saffron); }

  .brand-name {
    font-family: "Cinzel", serif; font-weight: 700; line-height: 1.05;
    text-align: center; letter-spacing: 0.02em;
  }
  .card--front .brand-name {
    position: absolute; left: 20px; top: 42px; width: 115px;
    font-size: 21px; color: var(--crimson);
  }
  .card--back .brand-name {
    position: absolute; left: 0; right: 0; top: 110px;
    font-size: 26px; color: var(--paper);
  }

  .building-motif {
    position: absolute; left: 0; top: 189px; width: 317px; height: 131px;
    background: linear-gradient(180deg, rgba(236,236,236,0) 0%, var(--faint) 70%, #e6e6e6 100%);
  }

  .holder-name {
    position: absolute; right: 51px; top: 96px;
    font-size: 22px; font-weight: 700; color: var(--ink); letter-spacing: 0.02em;
  }
  .holder-rule {
    position: absolute; left: 290px; top: 129px; width: 219px; height: 1.5px;
    background: var(--saffron);
  }

  .contact {
    position: absolute; right: 51px; top: 183px;
    text-align: right; font-size: 16.5px; line-height: 24px; color: var(--ink);
  }
  .contact .label { color: var(--crimson); font-weight: 700; }

  .accent-bar {
    position: absolute; left: 547px; top: 189px; width: 13px; height: 84px;
    background: var(--saffron);
  }

  .website {
    position: absolute; left: 0; right: 0; top: 263px;
    text-align: center; font-size: 13.5px; font-weight: 700;
    color: var(--paper); letter-spacing: 0.02em;
  }
</style>
</head>
<body>
<main class="canvas">
  <section class="card card--front" aria-label="Business card front">
    <div class="building-motif" role="img" aria-label="Faint line illustration of the palace building"></div>
    <div class="brand-name">Saffron<br>Lotus<br>Court</div>
    <h1 class="holder-name">Harjot Banwal</h1>
    <div class="holder-rule"></div>
    <address class="contact" style="font-style: normal;">
      <div><span class="label">Address:</span> 2917 West Tamarind Ave,</div>
      <div>Phoenix, Arizona, 85047</div>
      <div><span class="label">Phone:</span> (602) 517-3094</div>
      <div><span class="label">Fax:</span> (602) 768-2145</div>
    </address>
    <div class="accent-bar"></div>
  </section>

  <section class="card card--back" aria-label="Business card back">
    <div class="brand-name">Saffron<br>Lotus<br>Court</div>
    <div class="website">www.SaffronLotusCourt.example</div>
  </section>
</main>
</body>
</html>
```